Modern and Simple Supplement Label Design

We are looking for a Professional Graphic Designer who can design eye-catching and unique supplement label. We are supplement company who are sourcing different supplement products. I would like the design to be simple and with few colorsThe final design should communicate strength and growthI attached some samples for inspiration

Target Market(s)

Supplement Market - Collagen Supplements

Industry/Entity Type

Supplement

Font styles to use
Serif
Sans Serif

Colors

Designer to choose colors to be used in the design.

Requirements
Must have
• Front (Please search on Ombrix Collagen to get inspiration how to put together the front text)
• Logo: Velko Naturals
• Product Name: Duravita Blend Capsules
• Hydrolyzed type I II III V & X Collagen
• Dietary Supplements - 90 capsules
• Support Joints & bones
• Rejuvenate Skin
• Promotes Healthy Hair & Nails
• One right side supplement fact and left side precaution and instruction content. ( Please find the content of the right and left side of the bottle attached)
Nice to have
• Nice to have something that shows elements bring together to create something strong or beautiful. Our brand name is Velko Naturals. Velko is an assembly of beams or other elements that creates a rigid structure. This is to show our supplements help to provide the elements to have strong and healthy life

```html
<!DOCTYPE html>
<html lang="en">
<head>
<meta charset="utf-8">
<title>Velko Naturals – Duravita Blend Capsules Label</title>
<link rel="stylesheet" href="https://fonts.googleapis.com/css2?family=Roboto:ital,wght@0,400;0,700;0,900;1,700&family=Roboto+Condensed:wght@400&family=PT+Sans:wght@400&display=swap">
<style>
  :root {
    --navy: #34508f;
    --blue-mid: #3a66b6;
    --blue-light: #5f8fd6;
    --ink: #0d0d0d;
    --paper: #ffffff;
    --lavender: #e3e3f1;
  }
  * { margin: 0; padding: 0; box-sizing: border-box; }
  html, body { width: 1200px; height: 501px; overflow: hidden; }
  body {
    position: relative;
    background: linear-gradient(to bottom, var(--paper) 0%, var(--paper) 68%, var(--lavender) 100%);
    font-family: "PT Sans", sans-serif;
    color: var(--ink);
  }
  .pattern { position: absolute; left: 0; top: 0; width: 1200px; height: 501px; }

  /* side panels */
  .panel {
    position: absolute; top: 66px; width: 296px; height: 362px;
    background: var(--navy); color: var(--paper);
  }
  .panel-directions { left: 24px; clip-path: polygon(0 0, 264px 0, 296px 49px, 296px 100%, 0 100%); }
  .panel-facts { left: 873px; clip-path: polygon(30px 0, 100% 0, 100% 100%, 0 100%, 0 49px); }
  .panel > * { position: absolute; }
  .rule { height: 5px; background: var(--paper); }
  .panel-directions .rule { left: 31px; width: 225px; }
  .panel-facts .rule { left: 24px; width: 234px; }
  .heading-small { font-family: "Roboto", sans-serif; font-weight: 700; font-size: 10px; letter-spacing: .2px; }
  .copy { font-size: 7.6px; line-height: 9.8px; letter-spacing: -.1px; }
  .panel-directions .heading-small, .panel-directions .copy { left: 31px; width: 230px; }
  .barcode-area { left: 31px; top: 280px; width: 225px; height: 72px; background: var(--paper); }

  .facts-title { left: 33px; top: 22px; font-family: "Roboto", sans-serif; font-weight: 700; font-size: 19.5px; letter-spacing: .6px; }
  .serving { left: 33px; top: 56px; font-family: "Roboto", sans-serif; font-weight: 700; font-size: 8.8px; line-height: 12px; }
  .panel-facts .copy { left: 33px; width: 240px; }
  .amount { left: 185px !important; width: 60px !important; }
  .dose { left: 189px !important; width: 40px !important; }
  .dv-mark { left: 250px !important; width: 12px !important; }
  .seal { top: 286px; width: 48px; height: 48px; border-radius: 50%; background: var(--paper); }
  .seal-one { left: 27px; }
  .seal-two { left: 88px; }

  /* front */
  .front > * { position: absolute; text-align: center; white-space: nowrap; }
  .brand-name { left: 403px; width: 400px; top: 97px; font-family: "Roboto Condensed", sans-serif; font-size: 22px; letter-spacing: .5px; }
  .title { font-family: "Roboto", sans-serif; font-weight: 900; line-height: 1; }
  .title-one { left: 353px; width: 500px; top: 138px; font-size: 56px; }
  .title-two { left: 353px; width: 500px; top: 183px; font-size: 58px; letter-spacing: -.5px; }
  .title-three { left: 353px; width: 500px; top: 232px; font-size: 33px; }
  .spec { font-family: "Roboto", sans-serif; font-weight: 700; line-height: 1; }
  .spec-hydro { left: 464px; width: 160px; top: 276px; font-size: 12.5px; }
  .spec-type { left: 464px; width: 160px; top: 287px; font-size: 38px; font-weight: 900; }
  .spec-kinds { left: 464px; width: 160px; top: 325px; font-size: 19px; }
  .spec-collagen { left: 464px; width: 160px; top: 345px; font-size: 14px; }
  .spec-count { left: 599px; width: 120px; top: 289px; font-size: 44px; font-weight: 900; }
  .spec-caps { left: 599px; width 120px; width: 120px; top: 326px; font-size: 16.5px; }
  .spec-dietary { left: 589px; width: 140px; top: 342px; font-size: 8.2px; }
  .benefits { left: 404px; width: 400px; top: 373px; font-family: "Roboto", sans-serif; font-style: italic; font-weight: 700; font-size: 13px; line-height: 18.5px; letter-spacing: .3px; }
</style>
</head>
<body>

<svg class="pattern" viewBox="0 0 1200 501" role="img" aria-label="Blue geometric triangle pattern bands along the top and bottom edges">
  <defs>
    <linearGradient id="band" x1="0" x2="1" y1="0" y2="0">
      <stop offset="0" stop-color="#5f8fd6"/>
      <stop offset=".5" stop-color="#34508f"/>
      <stop offset="1" stop-color="#3a66b6"/>
    </linearGradient>
  </defs>
  <polygon fill="url(#band)" points="0,0 517,0 517,30 496,30 476,60 346,60 326,30 0,30"/>
  <polygon fill="url(#band)" points="684,0 1200,0 1200,30 872,30 852,60 714,60 684,30"/>
  <polygon fill="url(#band)" points="33,455 103,455 83,484 53,484"/>
  <polygon fill="url(#band)" points="138,455 324,455 344,484 119,484"/>
  <polygon fill="url(#band)" points="361,455 513,455 533,484 381,484"/>
  <polygon fill="url(#band)" points="583,455 688,455 673,484 568,484"/>
  <polygon fill="url(#band)" points="727,455 754,455 774,484 707,484"/>
  <polygon fill="url(#band)" points="826,455 910,455 890,484 846,484"/>
  <polygon fill="url(#band)" points="968,455 1167,455 1187,484 948,484"/>
</svg>

<section class="panel panel-directions" aria-label="Directions and cautions">
  <h2 class="heading-small" style="top:16px">SUGGESTED USE</h2>
  <p class="copy" style="top:27px">Take three (3) capsules one or more times a day or as directed by your health crae professional. For best results take on an empty stomach with an 8oz. glass of water.</p>
  <div class="rule" style="top:62px"></div>
  <h2 class="heading-small" style="top:78px">CAUTION</h2>
  <p class="copy" style="top:89px">Do not exceed recommended dose. Pregnant or nursing mothers, children under the age of 18, and individuals with a known medical condition should consult a physiciN BEFORE USING THIS OR ANY DIETRY SUPPLEMENT.</p>
  <div class="rule" style="top:130px"></div>
  <p class="copy" style="top:137px">KEEP OUT OF REACH OF CHILDREN.<br>DO NOT USE IF SAFETY SEAL IS DAMAGED OR MISSING.<br>STORE IN A COOL, DRY PLACE.</p>
  <div class="rule" style="top:182px"></div>
  <p class="copy" style="top:195px">* These statements have not been evaluated by the Food and Drug Administration. This product is not intended to diagnose, treat, cure or prevent any disease.</p>
  <div class="rule" style="top:232px"></div>
  <p class="copy" style="top:245px">LOT# and Expiration date printed on bottom of Bottle. V1R0</p>
  <div class="rule" style="top:264px"></div>
  <div class="barcode-area"></div>
</section>

<main class="front">
  <div class="brand-name">VELKO NATURALS</div>
  <h1 class="title title-one">DURAVITA</h1>
  <div class="title title-two">BLEND</div>
  <div class="title title-three">CAPSULES</div>
  <div class="spec spec-hydro">HYDROLYZED</div>
  <div class="spec spec-type">TYPE</div>
  <div class="spec spec-kinds">I II III V &amp; X</div>
  <div class="spec spec-collagen">COLLAGEN</div>
  <div class="spec spec-count">90</div>
  <div class="spec spec-caps">CAPSULES</div>
  <div class="spec spec-dietary">DIETARY SUPPLEMENTS</div>
  <p class="benefits">SUPPORTS JOINTS &amp; BONES<br>REJUVENATES SKIN<br>PROMOTES HEALTHY HAIR &amp; NAILS</p>
</main>

<section class="panel panel-facts" aria-label="Supplement facts">
  <h2 class="facts-title">SUPPLEMENT FACTS</h2>
  <p class="serving">SERVING SIZE: 3 CAPSULES<br>SERVINGS PER CONTAINER: 30</p>
  <div class="rule" style="top:84px"></div>
  <p class="copy amount" style="top:91px">AMOUNT PER<br>SERVING %0V</p>
  <p class="copy" style="top:116px">PREMIUM COLLAGEN<br>PROTEIN COMPLEX</p>
  <p class="copy dose" style="top:116px">1500mg</p>
  <p class="copy dv-mark" style="top:116px">**</p>
  <div class="rule" style="top:142px"></div>
  <p class="copy" style="top:155px">Bovine Collagen Peptides, Hydrolyzed Chicken Collagen Peptides, Pure Hydrolized Marine Collagen Peptides, Eggshell Membrane Collagen Peptides, Avian Sternum Collagen Peptides.</p>
  <div class="rule" style="top:193px"></div>
  <p class="copy" style="top:205px">** Daily Value not established (DV)</p>
  <p class="copy" style="top:230px">Inactive Ingredients: Gelatine Capsules<br>Contains: Egg, Fish<br>Contains no added: Milk, Tree Nuts, Wheat, Peanuts, Soy, Shellfish</p>
  <div class="rule" style="top:267px"></div>
  <div class="seal seal-one" role="img" aria-label="Certification seal"></div>
  <div class="seal seal-two" role="img" aria-label="Certification seal"></div>
</section>

</body>
</html>
```